Design a Brochure for Property project

Design 3 reports as a Brochure in Arabic language , each report ( brochure ) with the following requirement :

- 6-10 page A4 size for each .
- Add some HD image .
- Add the company logo and Contact .

for exampel the below brochure

```html
<!DOCTYPE html>
<html lang="ar" dir="rtl">
<head>
<meta charset="UTF-8">
<title>كتيب المشروع العقاري – الغلاف</title>
<link href="https://fonts.googleapis.com/css2?family=Cairo:wght@600;700;800&display=swap" rel="stylesheet">
<style>
  :root {
    --stage: #e9eaeb;
    --brand-blue: #2bb9ea;
    --brand-blue-deep: #1ba7db;
    --ink-white: #ffffff;
    --divider: #ffffff;
  }
  html, body {
    margin: 0;
    padding: 0;
    width: 1200px;
    height: 960px;
    overflow: hidden;
    background: var(--stage);
  }
  .spread {
    position: absolute;
    left: 50px;
    top: 91px;
    width: 1100px;
    height: 778px;
    background: linear-gradient(180deg, var(--brand-blue) 0%, var(--brand-blue-deep) 100%);
    overflow: hidden;
    box-shadow: 0 10px 30px rgba(0,0,0,0.18);
    font-family: "Cairo", Tahoma, sans-serif;
    color: var(--ink-white);
  }
  .spread__fold {
    position: absolute;
    left: 549px;
    top: 0;
    width: 2px;
    height: 100%;
    background: linear-gradient(90deg, rgba(0,0,0,0.08), rgba(255,255,255,0.08));
  }
  .photo-band {
    position: absolute;
    left: 0;
    top: 0;
    width: 1100px;
    height: 778px;
  }
  .brand {
    position: absolute;
    right: 70px;
    top: 48px;
    width: 400px;
    text-align: right;
  }
  .brand__name {
    margin: 0;
    font-size: 32px;
    font-weight: 700;
    line-height: 1.3;
  }
  .brand__slogan {
    margin: 4px 0 0;
    font-size: 19px;
    font-weight: 700;
    line-height: 1.3;
  }
  .back-message {
    position: absolute;
    left: 60px;
    width: 430px;
    top: 600px;
    text-align: center;
  }
  .back-message__years {
    margin: 0;
    font-size: 23px;
    font-weight: 700;
    line-height: 1.35;
  }
  .back-message__tagline {
    margin: 8px 0 0;
    font-size: 25px;
    font-weight: 700;
    line-height: 1.35;
  }
</style>
</head>
<body>
  <main class="spread">
    <svg class="photo-band" viewBox="0 0 1100 778" xmlns="http://www.w3.org/2000/svg">
      <defs>
        <linearGradient id="tone-living" x1="0" y1="0" x2="1" y2="1">
          <stop offset="0" stop-color="#c9d4d2"/>
          <stop offset="0.6" stop-color="#e8e4dc"/>
          <stop offset="1" stop-color="#b8a995"/>
        </linearGradient>
        <linearGradient id="tone-atrium" x1="0" y1="0" x2="1" y2="1">
          <stop offset="0" stop-color="#eef1f3"/>
          <stop offset="0.5" stop-color="#9fb6c9"/>
          <stop offset="1" stop-color="#e6e8ea"/>
        </linearGradient>
        <linearGradient id="tone-residence" x1="0" y1="0" x2="1" y2="1">
          <stop offset="0" stop-color="#d9d1c4"/>
          <stop offset="1" stop-color="#8c7a68"/>
        </linearGradient>
        <linearGradient id="tone-villa" x1="0" y1="0" x2="0" y2="1">
          <stop offset="0" stop-color="#c3d6e4"/>
          <stop offset="0.5" stop-color="#b9a48c"/>
          <stop offset="1" stop-color="#8a6a58"/>
        </linearGradient>
      </defs>
      <g stroke="var(--divider)" stroke-width="6" stroke-linejoin="miter">
        <polygon class="photo photo--living" role="img" aria-label="صورة: صالة معيشة مشرقة بأريكة وإطلالة على أفق المدينة"
          points="0,170 480,271 0,330" fill="url(#tone-living)"/>
        <polygon class="photo photo--atrium" role="img" aria-label="صورة: بهو داخلي أبيض بسقف معدني مقوس أزرق"
          points="0,346 500,275 720,322 380,456 0,370" fill="url(#tone-atrium)"/>
        <polygon class="photo photo--residence" role="img" aria-label="صورة: واجهة مبنى سكني مع باب مرآب"
          points="395,462 736,326 790,338 610,508" fill="url(#tone-residence)"/>
        <polygon class="photo photo--villa" role="img" aria-label="صورة: فلل بطراز متوسطي مع أشجار نخيل وسيارة متوقفة"
          points="806,341 1100,400 1100,620 628,513" fill="url(#tone-villa)"/>
      </g>
    </svg>

    <div class="spread__fold"></div>

    <header class="brand">
      <h1 class="brand__name">شعارك هنا</h1>
      <p class="brand__slogan">شعارك النصي هنا!</p>
    </header>

    <section class="back-message">
      <p class="back-message__years">نخدمكم منذ أكثر<br>من 20 عاماً</p>
      <p class="back-message__tagline">حسّن بيئة معيشتك<br>الخارجية</p>
    </section>
  </main>
</body>
</html>
```